Business cards - KESTO Roofing & Siding

We need simple business cards made up for our Roofing & Siding business based in Calgary Alberta.
The logo on one side of the card and potentially our slogan "Crafted with care, proven over years".
The other side could have:
-A small logo
-Rep name:
-Rep cell phone:
-Rep email:
-Office phone: 403-386-2049
-Website: PrairieShinglePros.com

We would like to incorporate the colours from our logo, especially the lite blue on the jpeg file. I have attached the ai file and jpeg file. We like the colours better on the jpeg file.

I do not require a money back guarantee

```html
<!DOCTYPE html>
<html lang="en">
<head>
<meta charset="utf-8">
<title>KESTO Roofing &amp; Siding – Business Cards</title>
<link href="https://fonts.googleapis.com/css2?family=Lato:wght@400;700&display=swap" rel="stylesheet">
<style>
  :root {
    --stage: #2a2a2a;
    --card: #ffffff;
    --sky-blue: #0a84e8;
    --deep-blue: #0566b5;
    --maple-red: #e81e25;
    --ink: #3c3c3c;
    --dark: #1e1e1e;
  }
  * { box-sizing: border-box; margin: 0; padding: 0; }
  html, body { width: 1200px; height: 1200px; overflow: hidden; }
  body {
    background: var(--stage);
    font-family: 'Lato', sans-serif;
    position: relative;
  }
  .card {
    position: absolute;
    left: 250px;
    width: 700px;
    height: 400px;
    background: var(--card);
    border-radius: 20px;
    overflow: hidden;
  }
  .card-front { top: 170px; }
  .card-back { top: 630px; }

  /* Front */
  .brand-small {
    position: absolute;
    right: 38px;
    top: 100px;
    display: flex;
    align-items: center;
    gap: 10px;
    font-size: 24px;
    font-weight: 700;
    color: var(--dark);
    letter-spacing: 0.5px;
  }
  .brand-mark {
    width: 18px;
    height: 18px;
    background: var(--sky-blue);
  }
  .rep-name {
    position: absolute;
    left: 38px;
    top: 188px;
    font-size: 31px;
    font-weight: 400;
    color: var(--sky-blue);
    letter-spacing: -0.3px;
  }
  .rep-title {
    position: absolute;
    left: 38px;
    top: 228px;
    font-size: 19px;
    color: var(--maple-red);
    letter-spacing: 0.3px;
  }
  .divider {
    position: absolute;
    left: 38px;
    right: 38px;
    top: 262px;
    height: 1.5px;
    background: var(--deep-blue);
  }
  .contact-list {
    position: absolute;
    left: 38px;
    top: 277px;
    list-style: none;
  }
  .contact-list li {
    display: flex;
    align-items: center;
    gap: 11px;
    height: 23.5px;
    font-size: 16px;
    color: var(--ink);
    letter-spacing: 0.3px;
  }
  .contact-list svg { width: 14px; height: 14px; fill: var(--sky-blue); flex: none; }
  .address {
    position: absolute;
    right: 38px;
    top: 277px;
    text-align: right;
    font-size: 16px;
    font-style: normal;
    line-height: 23.5px;
    color: var(--ink);
    letter-spacing: 0.3px;
  }
  .address .web { color: var(--sky-blue); }
  .footer-band {
    position: absolute;
    left: 0;
    bottom: 0;
    width: 700px;
    height: 22px;
    background: var(--deep-blue);
  }

  /* Back */
  .brand-large {
    position: absolute;
    left: 0;
    right: 0;
    top: 160px;
    display: flex;
    justify-content: center;
    align-items: center;
    gap: 16px;
    font-size: 40px;
    font-weight: 700;
    color: var(--dark);
    letter-spacing: 1px;
  }
  .brand-large .brand-mark { width: 28px; height: 28px; }
  .slogan {
    position: absolute;
    left: 0;
    right: 0;
    top: 342px;
    text-align: center;
    font-size: 19px;
    color: var(--ink);
    letter-spacing: 0.8px;
  }
  .slogan b { font-weight: 700; }
  .slogan .care { color: var(--sky-blue); font-weight: 700; }
  .slogan .years { color: var(--maple-red); font-weight: 700; }
</style>
</head>
<body>

<section class="card card-front">
  <div class="brand-small"><span class="brand-mark"></span>KESTO Roofing &amp; Siding</div>

  <h1 class="rep-name">DANIEL WHITFORD</h1>
  <p class="rep-title">Managing Director</p>
  <div class="divider"></div>

  <ul class="contact-list">
    <li>
      <svg viewBox="0 0 24 24"><path d="M6.6 10.8c1.4 2.8 3.8 5.1 6.6 6.6l2.2-2.2c.3-.3.7-.4 1-.2 1.1.4 2.3.6 3.6.6.6 0 1 .4 1 1V20c0 .6-.4 1-1 1C10.6 21 3 13.4 3 4c0-.6.4-1 1-1h3.5c.6 0 1 .4 1 1 0 1.3.2 2.5.6 3.6.1.3 0 .7-.2 1l-2.3 2.2z"/></svg>
      403-386-2049
    </li>
    <li>
      <svg viewBox="0 0 24 24"><path d="M7 2h10a2 2 0 0 1 2 2v16a2 2 0 0 1-2 2H7a2 2 0 0 1-2-2V4a2 2 0 0 1 2-2zm0 3v12h10V5H7zm5 13.5a1.2 1.2 0 1 0 0 2.4 1.2 1.2 0 0 0 0-2.4z"/></svg>
      403-386-2049
    </li>
    <li>
      <svg viewBox="0 0 24 24"><path d="M2 5h20v14H2V5zm2 2v.4l8 5.3 8-5.3V7H4zm0 2.8V17h16V9.8l-8 5.3-8-5.3z"/></svg>
      daniel@prairieshinglepros.com
    </li>
  </ul>

  <address class="address">
    2417 - 9 Avenue S.E.<br>
    Calgary, Alberta T2G 0V4<br>
    <span class="web">PrairieShinglePros.com</span>
  </address>

  <div class="footer-band"></div>
</section>

<section class="card card-back">
  <div class="brand-large"><span class="brand-mark"></span>KESTO Roofing &amp; Siding</div>
  <p class="slogan">CRAFTED <b>WITH</b> <span class="care">CARE</span>, PROVEN <b>OVER</b> <span class="years">YEARS</span></p>
</section>

</body>
</html>
```